Flier for digital rights event targetting TMVA trade negotiators

We need a design for an event that my organization (a nonprofit) is hosting with academic experts, to address government negotiators who are taking part in the 19th round of negotiations of the Coastal Integrated Commerce Accord (TMVA). Unfortunately we don't have the exact details yet such as who the speakers are, what date the meeting is, or even what location it is, other than that it will be in Hyderabad, India. So you will need to make a design with placeholder values that we can swap out later. Here is some information about TMVA: https://en.examplepedia.org/wiki/Coastal_Integrated_Commerce_Accord. The event will be called: "An Expert Roundtable on Electronic Commerce and TMVA". I'm attaching some similar fliers for previous events.

Target Market(s)

Government trade ministries

Industry/Entity Type

Trade

Font styles to use
Serif
Sans Serif

Colors

Designer to choose colors to be used in the design.

Requirements
Must have
• Space for organizer logos, including LKB logo from https://www.lkbnet.org/press/logos
Nice to have
• Space for headshots of speakers (even though we haven't finalized who they are yet)
Should not have
• Cheesy stock graphics

```html
<!DOCTYPE html>
<html lang="en">
<head>
<meta charset="utf-8">
<title>An Expert Roundtable on Electronic Commerce and TMVA</title>
<link rel="stylesheet" href="https://fonts.googleapis.com/css2?family=Saira+Semi+Condensed:wght@500;600&family=Open+Sans:wght@400;700&display=swap">
<style>
  :root {
    --page: #ece9e4;
    --red: #ed1c24;
    --red-deep: #c8161d;
    --orange: #f26a1b;
    --dark: #2a0d0b;
    --white: #ffffff;
    --ink-photo-a: #0d2a4a;
    --ink-photo-b: #5f8fb8;
  }
  * { box-sizing: border-box; margin: 0; padding: 0; }
  html, body { width: 1200px; height: 1200px; overflow: hidden; background: var(--page); }
  .flier {
    position: absolute; left: 40px; top: 204px; width: 1120px; height: 792px;
    background:
      radial-gradient(ellipse at 15% 55%, rgba(242,106,27,.85), transparent 45%),
      linear-gradient(180deg, var(--red) 0%, #e8371a 40%, #8a1a12 75%, var(--dark) 100%);
    box-shadow: 0 6px 18px rgba(0,0,0,.25);
  }
  .hero {
    position: absolute; left: 46px; top: 45px; width: 1029px; height: 345px;
    background:
      radial-gradient(circle at 82% 20%, rgba(220,235,250,.8), transparent 22%),
      radial-gradient(circle at 25% 35%, rgba(160,200,230,.5), transparent 25%),
      linear-gradient(120deg, var(--ink-photo-a) 0%, var(--ink-photo-b) 55%, #1b3a5e 100%);
  }
  .title-band {
    position: absolute; left: 46px; top: 255px; width: 1029px; height: 88px;
    background: var(--red);
    display: flex; align-items: center; justify-content: center;
  }
  .title-band h1 {
    font-family: "Saira Semi Condensed", sans-serif; font-weight: 600;
    font-size: 34px; color: var(--white); letter-spacing: .3px; text-transform: uppercase;
  }
  .details {
    position: absolute; left: 46px; top: 402px; width: 508px; height: 343px;
    background: var(--white); text-align: center;
    font-family: "Open Sans", sans-serif; color: var(--red);
  }
  .details h2 {
    margin: 18px 22px 0; padding-bottom: 4px; border-bottom: 1.5px solid var(--red);
    font-size: 21px; font-weight: 700; letter-spacing: .2px;
  }
  .details dl { margin-top: 12px; line-height: 20.5px; }
  .details dt { font-weight: 700; font-size: 18px; }
  .details dd { font-size: 18.5px; }
  .organisers {
    position: absolute; left: 20px; right: 20px; bottom: 24px;
    display: flex; justify-content: space-between; align-items: center;
  }
  .organiser {
    display: flex; align-items: center; gap: 6px;
    font-family: "Open Sans", sans-serif; font-weight: 700; font-size: 13px; color: #222;
  }
  .organiser .dot { width: 22px; height: 22px; border-radius: 50%; background: var(--red); }
  .organiser .dot.green { background: #2e9c8a; }
  .organiser .box { width: 18px; height: 18px; background: #222; }
  .about {
    position: absolute; left: 566px; top: 402px; width: 507px; height: 343px;
    background: var(--red); color: var(--white);
    padding: 24px 22px 0;
    font-family: "Open Sans", sans-serif; font-size: 13.4px; line-height: 14.6px;
    text-align: justify;
  }
  .about p + p { margin-top: 14px; }
</style>
</head>
<body>
  <main class="flier">
    <div class="hero" role="img" aria-label="Close-up photograph of a blue circuit board with soft bokeh lights"></div>
    <div class="title-band"><h1>An Expert Roundtable on Electronic Commerce and TMVA</h1></div>

    <section class="details">
      <h2>NINETEENTH ROUND OF NEGOTIATIONS</h2>
      <dl>
        <dt>WHEN</dt><dd>18–28 July 2017</dd>
        <dt>WHERE</dt><dd>Hyderabad, India</dd>
        <dt>TIME</dt><dd>12:30pm - 1:30pm</dd>
        <dt>RSVP</dt><dd>By 10 July 2017 to rsvp@lkbnet.org</dd>
      </dl>
      <div class="organisers">
        <div class="organiser"><span class="dot"></span>Liberty Knowledge Bureau</div>
        <div class="organiser"><span class="box"></span>Meridian Ministry of Foreign Trade</div>
        <div class="organiser"><span class="dot green"></span>tradelinks.net</div>
      </div>
    </section>

    <section class="about">
      <p>Coastal Integrated Commerce Accord (TMVA) is a proposed free trade agreement (FTA) between the ten member states of the Coastal Nations Forum (CNF) (Brunei, Cambodia, Indonesia, Laos, Malaysia, Myanmar, the Philippines, Singapore, Thailand, Vietnam) and the six states with which CNF has existing free trade agreements (Australia, China, India, Japan, South Korea and New Zealand).</p>
      <p>TMVA negotiations were formally launched in November 2012 at the CNF Summit in Cambodia. The agreement is scheduled to be finalized by the end of 2017. TMVA is viewed as an alternative to the Trans-Ocean Partnership (TOP), a proposed trade agreement which includes several Asian and American nations but excludes China and India.</p>
      <p>In 2017, prospective TMVA member states accounted for a population of 3.4 billion people with a total Gross Domestic Product (GDP, PPP) of $49.5 trillion, approximately 39 percent of the world's GDP,[4] with the combined GDPs of China and India making up more than half that amount.</p>
    </section>
  </main>
</body>
</html>
```